Bref créative
Business Card and Stationary for Hosting Company
Velmor
Professional
Tomas Hadley
General Manager
2815 Quillan Brook Road
Building 5 Suite 410
Marietta, GA 30182
tomash@brimtide.net
www.velmorhostingllc.com
Logo on the back
Please use this logo and let me know if you need anything else.

```html
<!DOCTYPE html>
<html lang="en">
<head>
<meta charset="utf-8">
<title>Velmor – Business Cards</title>
<link href="https://fonts.googleapis.com/css2?family=Open+Sans:wght@400;600;700&display=swap" rel="stylesheet">
<style>
  :root{
    --bg:#d9d9d7;
    --card-white:#ffffff;
    --orange:#f28c1e;
    --orange-deep:#e5701a;
    --blue:#2f82cc;
    --blue-deep:#1f6ab3;
    --ink:#4a4a4a;
    --ink-soft:#7a7a7a;
  }
  *{margin:0;padding:0;box-sizing:border-box}
  html,body{width:1200px;height:325px;overflow:hidden}
  body{background:var(--bg);font-family:"Open Sans",Arial,sans-serif;position:relative}
  .card{position:absolute;top:80px;width:260px;height:160px;border-radius:8px;overflow:hidden;box-shadow:0 3px 8px rgba(0,0,0,.18)}
  .card--front{background:var(--card-white)}
  .card--front-a{left:40px}
  .card--front-b{left:330px}
  .card--back-orange{left:640px;background:linear-gradient(135deg,var(--orange),var(--orange-deep))}
  .card--back-blue{left:910px;background:linear-gradient(135deg,var(--blue),var(--blue-deep))}
  .swoosh{position:absolute;right:0;top:0;width:90px;height:160px}
  .brand{position:absolute;left:18px;top:42px;display:flex;align-items:center;gap:6px}
  .brand__dot{width:16px;height:16px;border-radius:50%;background:var(--orange)}
  .brand__name{font-weight:700;font-size:22px;color:var(--blue);letter-spacing:.5px}
  .person{position:absolute;left:20px;top:92px}
  .person__name{font-size:11px;font-weight:600;color:var(--ink)}
  .person__title{font-size:7px;color:var(--ink-soft);margin-top:1px}
  .contact{position:absolute;left:128px;top:30px;list-style:none;font-size:5.5px;line-height:9px;color:var(--ink)}
  .contact li{display:flex;align-items:center;gap:3px}
  .contact svg{width:6px;height:6px;flex:none}
  .web-vertical{position:absolute;right:20px;top:80px;transform:translate(50%,-50%) rotate(-90deg);font-size:6.5px;color:#fff;white-space:nowrap;font-weight:600}
  .back-brand{position:absolute;left:50%;top:50%;transform:translate(-50%,-50%);display:flex;align-items:center;gap:8px}
  .back-brand__dot{width:22px;height:22px;border-radius:50%;background:#fff}
  .back-brand__name{font-weight:700;font-size:26px;color:#fff}
  .back-web{position:absolute;right:22px;top:80px;transform:translate(50%,-50%) rotate(-90deg);font-size:7px;color:#fff;white-space:nowrap}
</style>
</head>
<body>

  <section class="card card--front card--front-a">
    <svg class="swoosh" viewBox="0 0 90 160" aria-hidden="true">
      <path d="M60 0 C30 50 30 110 60 160 L90 160 L90 0Z" fill="var(--orange)"/>
      <path d="M72 0 C46 50 46 110 72 160 L90 160 L90 0Z" fill="var(--blue)"/>
    </svg>
    <div class="brand"><span class="brand__dot"></span><span class="brand__name">Velmor</span></div>
    <div class="person">
      <p class="person__name">Tomas Hadley</p>
      <p class="person__title">General Manager</p>
    </div>
    <ul class="contact">
      <li><svg viewBox="0 0 10 10"><path d="M5 0a3.5 3.5 0 0 0-3.5 3.5C1.5 6 5 10 5 10s3.5-4 3.5-6.5A3.5 3.5 0 0 0 5 0z" fill="var(--orange)"/></svg>2815 Quillan Brook Road</li>
      <li><span style="width:6px"></span>Building 5 Suite 410</li>
      <li><span style="width:6px"></span>Marietta, GA 30182</li>
      <li><svg viewBox="0 0 10 10"><rect x="2" y="0" width="6" height="10" rx="1.2" fill="var(--orange)"/></svg>770 555 0148</li>
      <li><svg viewBox="0 0 10 10"><rect x="0" y="2" width="10" height="6" fill="var(--orange)"/></svg>tomash@brimtide.net</li>
    </ul>
    <span class="web-vertical">www.velmorhostingllc.com</span>
  </section>

  <section class="card card--front card--front-b">
    <svg class="swoosh" viewBox="0 0 90 160" aria-hidden="true">
      <path d="M60 0 C30 50 30 110 60 160 L90 160 L90 0Z" fill="var(--orange)"/>
      <path d="M72 0 C46 50 46 110 72 160 L90 160 L90 0Z" fill="var(--blue)"/>
    </svg>
    <div class="brand"><span class="brand__dot"></span><span class="brand__name">Velmor</span></div>
    <div class="person">
      <p class="person__name">Tomas Hadley</p>
      <p class="person__title">General Manager</p>
    </div>
    <ul class="contact">
      <li><svg viewBox="0 0 10 10"><path d="M5 0a3.5 3.5 0 0 0-3.5 3.5C1.5 6 5 10 5 10s3.5-4 3.5-6.5A3.5 3.5 0 0 0 5 0z" fill="var(--orange)"/></svg>2815 Quillan Brook Road</li>
      <li><span style="width:6px"></span>Building 5 Suite 410</li>
      <li><span style="width:6px"></span>Marietta, GA 30182</li>
      <li><svg viewBox="0 0 10 10"><rect x="2" y="0" width="6" height="10" rx="1.2" fill="var(--orange)"/></svg>770 555 0148</li>
      <li><svg viewBox="0 0 10 10"><rect x="0" y="2" width="10" height="6" fill="var(--orange)"/></svg>tomash@brimtide.net</li>
    </ul>
    <span class="web-vertical">www.velmorhostingllc.com</span>
  </section>

  <section class="card card--back-orange">
    <div class="back-brand"><span class="back-brand__dot"></span><span class="back-brand__name">Velmor</span></div>
    <span class="back-web">www.velmorhostingllc.com</span>
  </section>

  <section class="card card--back-blue">
    <div class="back-brand"><span class="back-brand__dot"></span><span class="back-brand__name">Velmor</span></div>
    <span class="back-web">www.velmorhostingllc.com</span>
  </section>

</body>
</html>
```